Country House in Italy Needs a Business Card Design

We need a business card design for “Casale del Ruscello”, a modern concept of a Farm Holidays/Country House to be opened in central Italy.
Attached is the company logo you did for us in the past.
Please
- create a double-sided business card design
- on the back I would like to have the logo
- on the front the copy
Copy on card:
o Casale del Ruscello
o Address: Via Fontalba, 14
Cingoli (MC), Italy
o Website: www.casaledelruscello.it
o Email: info@casaledelruscello.it
o my name : Lucilla
o my mobile phone number: +39 347 8124591
In the distribution of information keep in mind the possible inclusion also of a landline telephone number (currently not available / existing).
WE WOULD LIKE TO HAVE A MODERN, PROFFESIONAL, OUT OF THE BOX BUSINESS CARD. BE AS CREATIVE AS YOU WOULD LIKE.

```html
<!DOCTYPE html>
<html lang="it">
<head>
<meta charset="utf-8">
<title>Casale del Ruscello – Business Card</title>
<link href="https://fonts.googleapis.com/css2?family=Gelasio:wght@400&family=Exo+2:wght@400;500;700&display=swap" rel="stylesheet">
<style>
  :root{
    --stage:#e9e8e6;
    --card:#fdfdfd;
    --ink:#4f4a47;
    --ink-soft:#6b6461;
    --orange:#e8733a;
    --gold-light:#f0cf9f;
    --gold:#d9a86e;
    --gold-deep:#c48f55;
  }
  *{margin:0;padding:0;box-sizing:border-box}
  html,body{width:1200px;height:901px;overflow:hidden;background:var(--stage)}
  .canvas{position:relative;width:1200px;height:901px}
  .card{
    position:absolute;top:296px;width:540px;height:309px;
    background:var(--card);border-radius:26px;overflow:hidden;
    box-shadow:0 2px 0 #cfcfcf,0 14px 30px rgba(0,0,0,.12);
  }
  .card--front{left:45px}
  .card--back{left:615px}

  .brand-mark{position:absolute;border-radius:50%;
    background:radial-gradient(circle,var(--gold-light),var(--gold) 60%,var(--orange));}
  .card--front .brand-mark{left:40px;top:34px;width:78px;height:78px}
  .brand{position:absolute;font-family:"Gelasio",Georgia,serif}
  .brand__name{display:block;color:var(--ink);font-size:29px;line-height:1.1}
  .brand__tag{display:block;font-family:"Exo 2",Arial,sans-serif;color:var(--orange);
    font-size:11px;letter-spacing:.14em;margin-top:4px}
  .card--front .brand{left:138px;top:50px}

  .person{position:absolute;left:40px;top:138px;font-family:"Exo 2",Arial,sans-serif}
  .person__name{color:var(--orange);font-weight:700;font-size:17px;letter-spacing:.06em}
  .person__role{color:var(--ink-soft);font-size:11px;margin-top:3px}
  .person__address{color:var(--ink);font-size:11.5px;line-height:1.5;margin-top:12px;font-style:normal}

  .contacts{position:absolute;right:36px;top:146px;list-style:none;
    font-family:"Exo 2",Arial,sans-serif;font-size:12.5px;color:var(--ink);text-align:right}
  .contacts li{display:flex;justify-content:flex-end;align-items:center;gap:9px;height:21px}
  .contacts svg{width:13px;height:13px;fill:var(--orange);flex:none}

  .wave{position:absolute;left:0;bottom:0;width:540px;height:309px}

  .card--back .brand-mark{left:222px;top:64px;width:96px;height:96px}
  .card--back .brand{left:0;right:0;top:178px;text-align:center}
  .card--back .brand__name{font-size:30px}
</style>
</head>
<body>
<main class="canvas">

  <section class="card card--front" aria-label="Front of business card">
    <svg class="wave" viewBox="0 0 540 309" aria-hidden="true">
      <defs>
        <linearGradient id="goldBand" x1="0" y1="0" x2="1" y2="0">
          <stop offset="0" stop-color="var(--gold-deep)"/>
          <stop offset=".5" stop-color="var(--gold-light)"/>
          <stop offset="1" stop-color="var(--gold)"/>
        </linearGradient>
      </defs>
      <path d="M0,222 C110,196 230,238 360,309 L0,309 Z" fill="url(#goldBand)"/>
      <path d="M120,226 C200,236 260,262 320,309" fill="none" stroke="#fff" stroke-width="3" opacity=".8"/>
    </svg>

    <span class="brand-mark" aria-hidden="true"></span>
    <h1 class="brand">
      <span class="brand__name">Casale del Ruscello</span>
      <span class="brand__tag">COUNTRY HOUSE</span>
    </h1>

    <div class="person">
      <p class="person__name">PAOLO FERRANTE</p>
      <p class="person__role">Managing Director</p>
      <address class="person__address">072 9th floor/Hall<br>Meadow Road CNG</address>
    </div>

    <ul class="contacts">
      <li>014 362 5087
        <svg viewBox="0 0 16 16" aria-label="Phone"><path d="M3 1h3l1.5 4-2 1.3a9 9 0 0 0 4.2 4.2L11 8.5l4 1.5v3a2 2 0 0 1-2 2A12 12 0 0 1 1 3a2 2 0 0 1 2-2z"/></svg></li>
      <li>014 362 5087
        <svg viewBox="0 0 16 16" aria-label="Mobile"><path d="M4 0h8a1 1 0 0 1 1 1v14a1 1 0 0 1-1 1H4a1 1 0 0 1-1-1V1a1 1 0 0 1 1-1zm1 2v10h6V2zm3 11a1 1 0 1 0 0 2 1 1 0 0 0 0-2z"/></svg></li>
      <li>014 362 5087
        <svg viewBox="0 0 16 16" aria-label="Fax"><path d="M4 0h8v4H4zM1 5h14v7h-3v4H4v-4H1zm4 5v5h6v-5z"/></svg></li>
      <li>info@casaledelruscello.it
        <svg viewBox="0 0 16 16" aria-label="Email"><path d="M0 3h16v10H0zm1.5 1.2L8 9l6.5-4.8V4h-13z"/></svg></li>
      <li>www.casaledelruscello.it
        <svg viewBox="0 0 16 16" aria-label="Website"><path d="M8 0a8 8 0 1 0 0 16A8 8 0 0 0 8 0zm0 1.5c.8 0 1.8 1.7 2.1 4.5H5.9C6.2 3.2 7.2 1.5 8 1.5zM1.6 7h2.9v2H1.6a6.5 6.5 0 0 1 0-2zm4.3 0h4.2v2H5.9zm5.6 0h2.9a6.5 6.5 0 0 1 0 2h-2.9zM5.9 10h4.2c-.3 2.8-1.3 4.5-2.1 4.5S6.2 12.8 5.9 10z"/></svg></li>
    </ul>
  </section>

  <section class="card card--back" aria-label="Back of business card">
    <span class="brand-mark" aria-hidden="true"></span>
    <h2 class="brand">
      <span class="brand__name">Casale del Ruscello</span>
      <span class="brand__tag">COUNTRY HOUSE</span>
    </h2>
  </section>

</main>
</body>
</html>
```